Sponsor at Title Insurance Industry Seminar for Continuing Ed - 250 Companies in Attendance

I offer escrow accounting services in the Title Insurance Industry. I've attached logo files and an example of my former company. I don't like the design and it's a little wordy but it provides detail of what I offer.

Below is a brief write-up...
For professionals in the title insurance industry, finding a reliable and cost-effective solution to escrow accounting needs can feel overwhelming. When choosing the right accounting partner, title companies and law firms need a group they can trust, and that’s where we come in. Brightfen Ledger Works is a team that understands the title industry and the importance of compliance, security and accuracy. Brightfen Ledger Works is the experienced, convenient and cost-effective choice for the accounting and certification needs of companies throughout the country.

```html
<!DOCTYPE html>
<html lang="en">
<head>
<meta charset="utf-8">
<title>Brightfen Ledger Works – Escrow Accounting Services</title>
<link rel="stylesheet" href="https://fonts.googleapis.com/css2?family=Jost:wght@300;400;500;600;700&display=swap">
<style>
  :root {
    --backdrop: #6b6c71;
    --paper: #ffffff;
    --navy: #363f4f;
    --copper: #b9705c;
    --copper-light: #d69a86;
    --blush: #dbb3a8;
    --copper-shine: #f5c6b2;
    --copper-deep: #a26b5c;
    --teal: #1f8298;
    --teal-dark: #0f2732;
    --white: #ffffff;
  }
  * { margin: 0; padding: 0; box-sizing: border-box; }
  html, body { width: 904px; height: 1200px; overflow: hidden; background: var(--backdrop); }
  body { position: relative; font-family: "Jost", "Futura", sans-serif; }

  .flyer {
    position: absolute; left: 73.8px; top: 95px;
    width: 1376px; height: 1780px;
    transform: scale(0.5426); transform-origin: 0 0;
    background: var(--paper); overflow: hidden; color: var(--navy);
  }

  .brand { position: absolute; left: 44px; top: 30px; width: 400px; text-align: center; }
  .brand-dot { width: 110px; height: 110px; border-radius: 50%; background: var(--copper); margin: 0 auto 34px; }
  .brand-name { font-weight: 500; font-size: 54px; line-height: 1.08; color: var(--copper); letter-spacing: 1px; }

  .copper-ribbon {
    position: absolute; left: 464px; top: 0; width: 293px; height: 265px; z-index: 3;
    background: linear-gradient(90deg, var(--copper-deep) 0%, var(--copper-shine) 50%, var(--copper-deep) 100%);
  }

  .hero-photo {
    position: absolute; left: 609px; top: 0; width: 767px; height: 1075px; z-index: 2;
    border-bottom-left-radius: 260px 465px;
    background: radial-gradient(ellipse at 55% 60%, var(--teal) 0%, #185a6c 38%, var(--teal-dark) 85%);
  }

  .contact-panel {
    position: absolute; left: 696px; top: 900px; width: 680px; height: 880px; z-index: 1;
    background: var(--navy); border-bottom-left-radius: 160px;
  }

  .headline { position: absolute; left: 42px; top: 330px; font-size: 96px; line-height: 84px; font-weight: 600; }
  .headline .accent { font-weight: 400; color: var(--copper); }

  .subject-band {
    position: absolute; left: 0; top: 603px; width: 612px; height: 146px;
    background: var(--navy); color: var(--white);
    font-weight: 300; font-size: 50px; line-height: 54px; padding: 18px 0 0 48px;
  }

  .about { position: absolute; left: 42px; top: 772px; width: 556px; }
  .about h2 { font-size: 56px; font-weight: 600; color: var(--copper); line-height: 64px; }
  .about p {
    margin-top: 12px; font-size: 32px; font-weight: 500; letter-spacing: 0.8px;
    line-height: 49.5px; text-align: justify; hyphens: auto;
  }

  .promise-band {
    position: absolute; left: 0; top: 1248px; width: 696px; height: 215px;
    background: var(--blush); padding: 10px 0 0 42px;
    font-size: 45px; font-weight: 500; line-height: 65px;
  }

  .services { position: absolute; left: 0; top: 1480px; }
  .services h2 { margin-left: 42px; font-size: 56px; font-weight: 600; line-height: 64px; }
  .services ul { list-style: none; margin-top: 8px; }
  .services li {
    position: relative; padding-left: 56px; height: 72px;
    font-size: 38px; font-weight: 500; letter-spacing: 2.4px; color: var(--copper); line-height: 56px;
  }
  .services li::before {
    content: ""; position: absolute; left: 0; top: 21px; width: 45px; height: 14px;
    background: var(--navy); border-radius: 0 7px 7px 0;
  }

  .benefits { position: absolute; left: 731px; top: 1108px; width: 603px; z-index: 3; }
  .benefits p {
    font-size: 34px; font-weight: 300; letter-spacing: 2px; line-height: 36px;
    color: var(--copper-light); text-align: justify; text-align-last: left;
  }
  .benefits ul { list-style: none; margin-top: 14px; }
  .benefits li { font-size: 42px; font-weight: 600; letter-spacing: 2.4px; color: var(--white); line-height: 61px; }
  .benefits hr { border: 0; height: 3px; background: var(--white); margin-top: 8px; width: 610px; }

  .contact-icons { position: absolute; left: 747px; top: 1492px; z-index: 3; list-style: none; }
  .contact-icons li { width: 52px; height: 52px; margin-bottom: 34px; }
  .contact-icons svg { display: block; width: 52px; height: 52px; }
</style>
</head>
<body>
<main class="flyer">
  <div class="brand">
    <div class="brand-dot"></div>
    <div class="brand-name">Brightfen<br>Ledger Works</div>
  </div>

  <div class="copper-ribbon"></div>
  <div class="hero-photo" role="img" aria-label="Photo of hands holding a tablet showing a glowing blue financial statistics dashboard"></div>
  <div class="contact-panel"></div>

  <h1 class="headline">Escrow<br>Accounting<br><span class="accent">Services</span></h1>

  <div class="subject-band">in the Title<br>Insurance Industry</div>

  <section class="about">
    <h2>Who We Are</h2>
    <p>Brightfen Ledger Works is a team that understands the title industry and the importance of compliance, security and accuracy. When choosing the right accounting partner, title companies and law firms need a group they can trust, and that’s where we come in.</p>
  </section>

  <div class="promise-band">Our team of experienced<br>professionals can be your<br>perfect solution!</div>

  <section class="services">
    <h2>Our Services</h2>
    <ul>
      <li>Escrow Reconciliation Services</li>
      <li>Title Best Practice Certification</li>
      <li>Other Related Services</li>
    </ul>
  </section>

  <section class="benefits">
    <p>Put Brightfen Ledger Works knowledge and experience to work for you. We want to help you achieve:</p>
    <ul>
      <li>- 100% Compliance</li>
      <li>- 100% Convenience</li>
      <li>- 100% Credibility</li>
    </ul>
    <hr>
  </section>

  <ul class="contact-icons">
    <li><svg viewBox="0 0 52 52" aria-label="Phone"><circle cx="26" cy="26" r="25" fill="#dbb3a8"/><path d="M18 14c2-1 4 0 5 2l2 4c1 2 0 3-1 4l-1 1c1 3 4 6 7 7l1-1c1-1 2-2 4-1l4 2c2 1 3 3 2 5-1 2-3 3-5 3-9-1-18-10-19-19 0-3 0-5 1-7z" fill="#363f4f"/></svg></li>
    <li><svg viewBox="0 0 52 52" aria-label="Email"><circle cx="26" cy="26" r="25" fill="#dbb3a8"/><text x="26" y="36" text-anchor="middle" font-family="Jost, sans-serif" font-size="30" font-weight="500" fill="#363f4f">@</text></svg></li>
    <li><svg viewBox="0 0 52 52" aria-label="Website"><circle cx="26" cy="26" r="25" fill="#dbb3a8"/><g fill="none" stroke="#363f4f" stroke-width="2"><circle cx="26" cy="26" r="13"/><ellipse cx="26" cy="26" rx="6" ry="13"/><path d="M13 26h26M15 20h22M15 32h22"/></g></svg></li>
  </ul>
</main>
</body>
</html>
```